Letterhead for louvre roof company in NZ

I require a letter head design for a company called Skyvane Group.
I would like a footer to the letter head and possibly a water mark.
See attached logo.

```html
<!DOCTYPE html>
<html lang="en">
<head>
<meta charset="utf-8">
<title>Skyvane Group Letterhead</title>
<link rel="stylesheet" href="https://fonts.googleapis.com/css2?family=Lato:wght@400&family=Open+Sans:wght@400;600&display=swap">
<style>
  :root {
    --brand-orange: #f0861f;
    --text-grey: #4a4a4a;
    --text-dark: #222222;
    --rule-grey: #9a9a9a;
    --paper: #ffffff;
  }
  * { margin: 0; padding: 0; box-sizing: border-box; }
  html, body {
    width: 1040px;
    height: 1200px;
    overflow: hidden;
    background: var(--paper);
  }
  .letterhead {
    position: relative;
    width: 1040px;
    height: 1200px;
    background: var(--paper);
    font-family: "Open Sans", Arial, sans-serif;
    color: var(--text-grey);
  }
  .band {
    position: absolute;
    left: 0;
    width: 100%;
    height: 18px;
    background: var(--brand-orange);
  }
  .band--top { top: 0; }
  .band--bottom { bottom: 0; }

  .brand {
    position: absolute;
    top: 46px;
    left: 0;
    width: 100%;
    display: flex;
    flex-direction: column;
    align-items: center;
    gap: 10px;
  }
  .brand__square {
    width: 72px;
    height: 72px;
    background: var(--brand-orange);
  }
  .brand__name {
    font-family: "Open Sans", Arial, sans-serif;
    font-weight: 600;
    font-size: 16px;
    color: var(--brand-orange);
    letter-spacing: 0.3px;
  }

  .letter {
    position: absolute;
    left: 98px;
    width: 842px;
    font-size: 16.5px;
  }
  .letter__date { top: 249px; }
  .letter__recipient { top: 283px; line-height: 19px; font-style: normal; }
  .letter__salutation { top: 386px; }
  .letter__body { top: 439px; }
  .letter__body p {
    line-height: 27px;
    text-align: justify;
    hyphens: auto;
    margin-bottom: 27px;
  }
  .letter__closing { top: 845px; }
  .letter__signatory { top: 920px; }
  .signatory__name {
    font-size: 20px;
    font-weight: 600;
    color: var(--text-dark);
  }
  .signatory__title {
    font-size: 16.5px;
    margin-top: 4px;
  }

  .footer {
    position: absolute;
    left: 99px;
    width: 832px;
    top: 1117px;
    font-family: "Lato", Arial, sans-serif;
    font-size: 18px;
    color: var(--text-dark);
    text-align: center;
  }
  .footer__contacts { padding-bottom: 6px; border-bottom: 1.5px solid var(--rule-grey); }
  .footer__label, .footer__web { color: var(--brand-orange); }
  .footer__sep { margin: 0 8px; }
  .footer__address { margin-top: 6px; }
</style>
</head>
<body>
  <main class="letterhead">
    <div class="band band--top"></div>

    <header class="brand">
      <div class="brand__square"></div>
      <div class="brand__name">Skyvane Group</div>
    </header>

    <p class="letter letter__date">Issuing Date: May 5, 2018</p>

    <address class="letter letter__recipient">
      Name Of Employee Mr. XYZABC<br>
      Address of Employee<br>
      Address Line 2 etc..
    </address>

    <p class="letter letter__salutation">Dear Mr.XYZABC</p>

    <section class="letter letter__body" lang="en">
      <p>Lorem Ipsum has been the industry's standard dummy text ever since the 1500s, when an unknown printer took a galley of type and scrambled it to make a type specimen book. It has survived not only five centuries, but also the leap into electronic typesetting, remaining essentially unchanged. It was popularised in the 1960s with the release of Typeline sheets containing Lorem Ipsum passages, and more recently with desktop publishing software like Pagecraft Studio including versions of Lorem Ipsum.</p>
      <p>Lorem Ipsum is simply dummy text of the printing and typesetting industry. Lorem Ipsum has been the industry's standard dummy text ever since the 1500s, when an unknown printer took a galley of type and scrambled it to make a type specimen book.</p>
      <p>It has survived not only five centuries, but also the leap into electronic typesetting, remaining essentially unchanged. It was popularised in the 1960s with the release of Typeline sheets containing Lorem IpsumIpsum passages.</p>
    </section>

    <p class="letter letter__closing">Yours Sincerely</p>

    <div class="letter letter__signatory">
      <div class="signatory__name">Daniel Carter</div>
      <div class="signatory__title">Managing Director</div>
    </div>

    <footer class="footer">
      <div class="footer__contacts">
        <span class="footer__label">P:</span> 09-555 018 247<span class="footer__sep">|</span><span class="footer__label">E:</span> hello@skyvanemail.co.nz<span class="footer__sep">|</span><span class="footer__web">www.skyvanesite.co.nz</span>
      </div>
      <div class="footer__address">58 Harbour Lane, Auckland 1010, New Zealand</div>
    </footer>

    <div class="band band--bottom"></div>
  </main>
</body>
</html>
```